Gather Every Meadow Gala Graphic Design

I’m seeking a professional graphic designer experienced in event branding to create a cohesive suite of materials for our third annual fundraising gala, “Gather Every Meadow.” This year's theme is " A Dance in Green to Gather Every Meadow" Need to design collateral for website, social media and email blasts.
Target Market(s)
Affluent gala attendees
Industry/Entity Type
Fundraising / Charity / Outdoors / Sports
Font styles to use
Decorative
Script
Colors
0054AA
0677BA
7BADD7
CADEEF
E8F1F8
0094D4
00A9DD
6FCCEA
C7EBF8
E9F6FB
00AB8E
00BBA5
67D7C9
C6EFE9
E9F9F6
6B429C
8869AF
B7A5CE
E3DAEB
F3F0F8

```html
<!DOCTYPE html>
<html lang="en">
<head>
<meta charset="utf-8">
<title>A Dance in Green to Gather Every Meadow</title>
<link rel="stylesheet" href="https://fonts.googleapis.com/css2?family=Playfair+Display:wght@600;700&family=Great+Vibes&family=Poppins:wght@300;500;600&family=Oswald:wght@500&display=swap">
<style>
  :root {
    --page: #ffffff;
    --night: #0c1838;
    --night-mid: #1b2c5c;
    --sea-deep: #0f2f3d;
    --sea: #167a72;
    --green: #12ae8e;
    --green-bright: #00bba5;
    --mist: #cadeef;
    --white: #ffffff;
  }
  * { margin: 0; padding: 0; box-sizing: border-box; }
  html, body {
    width: 1081px; height: 1200px; overflow: hidden;
    background: var(--page);
  }
  .invite {
    position: absolute; left: 160px; top: 220px;
    width: 773px; height: 773px; overflow: hidden;
    background: var(--green);
  }
  .scene-photo {
    position: absolute; inset: 0;
    background:
      radial-gradient(ellipse 40px 30px at 388px 82px, rgba(255,240,200,.9), transparent 70%),
      linear-gradient(180deg, var(--night) 0%, var(--night-mid) 56%, #16263f 58%, var(--sea-deep) 64%, var(--sea) 82%, var(--green) 100%);
  }
  .title-art { position: absolute; left: 0; top: 0; width: 773px; height: 480px; }
  .title-kicker {
    font-family: "Playfair Display", serif; font-weight: 700;
    font-size: 62px; fill: var(--white); letter-spacing: 2px;
  }
  .title-main {
    font-family: "Playfair Display", serif; font-weight: 700;
    font-size: 300px;
  }
  .title-script {
    font-family: "Great Vibes", cursive; font-size: 74px; fill: var(--mist);
  }
  .details {
    position: absolute; left: 0; right: 0; top: 474px;
    text-align: center; color: var(--white);
    font-family: "Poppins", sans-serif;
  }
  .lead { font-weight: 300; font-size: 17px; line-height: 24px; }
  .anniversary {
    display: inline-block; margin-top: 10px;
    width: 291px; height: 52px; border-radius: 8px;
    background: var(--green);
    box-shadow: 0 0 12px rgba(103,215,201,.6);
    font-family: "Great Vibes", cursive; font-size: 38px; line-height: 54px;
  }
  .venue-name { font-weight: 300; font-size: 17px; margin-top: 6px; line-height: 26px; }
  .date { font-weight: 600; font-size: 29px; line-height: 30px; margin-top: 2px; }
  .time { font-weight: 600; font-size: 24px; line-height: 28px; }
  .address { font-weight: 600; font-size: 20px; line-height: 30px; }
  .attire {
    display: inline-block; margin-top: 6px;
    padding: 0 12px; height: 20px; border-radius: 10px;
    background: var(--white); color: var(--green);
    font-family: "Oswald", sans-serif; font-weight: 500; font-size: 13px; line-height: 20px;
    letter-spacing: .5px;
  }
  .tickets {
    position: absolute; left: 8px; right: 8px; top: 716px; height: 35px;
    background: linear-gradient(90deg, rgba(255,255,255,0) 0%, rgba(255,255,255,.85) 22%, #f4faf9 50%, rgba(255,255,255,.85) 78%, rgba(255,255,255,0) 100%);
    text-align: center;
    font-family: "Poppins", sans-serif; font-weight: 600; font-size: 20px; line-height: 35px;
    color: var(--green);
  }
</style>
</head>
<body>
  <main class="invite">
    <div class="scene-photo" role="img" aria-label="Photograph of a lit offshore lighthouse on iron legs under a starry night sky above calm turquoise water"></div>

    <svg class="title-art" viewBox="0 0 773 480" aria-label="A Dance in Green to Gather Every Meadow">
      <defs>
        <linearGradient id="title-fade" x1="0" y1="0" x2="0" y2="1">
          <stop offset="0" stop-color="#ffffff"/>
          <stop offset=".55" stop-color="#e9f1f8"/>
          <stop offset="1" stop-color="#7badd7" stop-opacity=".25"/>
        </linearGradient>
      </defs>
      <text class="title-kicker" x="386" y="196" text-anchor="middle" textLength="316" lengthAdjust="spacingAndGlyphs">A DANCE IN</text>
      <text class="title-main" x="386" y="430" text-anchor="middle" fill="url(#title-fade)" textLength="583" lengthAdjust="spacingAndGlyphs">GREEN</text>
      <text class="title-script" x="386" y="440" text-anchor="middle" textLength="500" lengthAdjust="spacingAndGlyphs">to Gather Every Meadow</text>
    </svg>

    <section class="details">
      <p class="lead">Join us for an unforgettable evening as we celebrate the</p>
      <p class="anniversary">150th Anniversary</p>
      <p class="venue-name">of the Heron Point Beacon!</p>
      <p class="date">NOVEMBER 18, 2023</p>
      <p class="time">COCKTAILS AT 6:00 PM</p>
      <p class="address">Willow Cay - 4120 Harbor Loop, Bayhaven</p>
      <p class="attire">COCKTAIL ATTIRE</p>
    </section>

    <p class="tickets">Get Your Tickets Today!</p>
  </main>
</body>
</html>
```